Website Design for Employee Moral and Happiness Company

Looking for a clean website design that explains our features in a step by step manner so our visitors know exactly what our site does before logging in.

The site is called "Velquo". See logo design and video for a sample of style and an overview of what we do.

Target Market(s)

Business owners that are looking to retain employees.

Number of Pages Required

1 page

```html
<!DOCTYPE html>
<html lang="en">
<head>
<meta charset="utf-8">
<title>Velquo – Employee Recognition Platform</title>
<link href="https://fonts.googleapis.com/css2?family=Lexend:wght@400;500;600;700&family=Montserrat:ital,wght@0,400;0,500;0,600;1,600;1,700&display=swap" rel="stylesheet">
<style>
:root{
  --orange:#f47320;
  --orange-dark:#e0601a;
  --ink:#1b1b1b;
  --navy:#243a5e;
  --muted:#6d6a66;
  --hero-bg:#efe9e1;
  --beige:#ebe4da;
  --cream:#f7f3ec;
  --testi-bg:#fdf0dc;
  --grey-block:#c6beb2;
  --white:#ffffff;
}
*{box-sizing:border-box;margin:0;padding:0}
html,body{width:1200px;height:5319px;overflow:hidden}
body{font-family:"Montserrat",sans-serif;color:var(--ink);background:var(--white)}
section,header,footer{position:relative;width:1200px;overflow:hidden}
.abs{position:absolute;z-index:2}
.art{position:absolute;z-index:1}
h1,h2,h3{font-family:"Lexend",sans-serif;font-weight:600;color:var(--ink)}
.accent{color:var(--orange)}
.btn{position:absolute;z-index:2;display:flex;align-items:center;justify-content:center;font-family:"Montserrat",sans-serif;font-weight:600;font-size:18px;letter-spacing:.3px;border-radius:4px;text-transform:uppercase}
.btn-orange{background:var(--orange);color:var(--white)}
.btn-white{background:var(--white);color:var(--ink)}
.btn-outline{border:2px solid var(--white);color:var(--white)}
.body-text{font-size:15.5px;line-height:27px;color:var(--muted)}

/* Hero */
.hero{height:673px;background:var(--hero-bg)}
.logo{font-family:"Lexend",sans-serif;font-weight:700;color:var(--ink);letter-spacing:1px}
.hero .logo{left:111px;top:26px;font-size:56px}
.nav{left:395px;top:52px;display:flex;gap:19px;font-size:17px;font-weight:500}
.login{left:815px;top:52px;font-size:17px;font-weight:500;display:flex;align-items:center;gap:6px}
.hero .btn-nav{left:900px;top:42px;width:188px;height:48px;font-size:16px}
.hero h1{left:111px;top:240px;width:500px;font-size:50px;line-height:60px;font-weight:600}
.hero .btn-hero{left:111px;top:475px;width:226px;height:64px}
.hero .art{left:620px;top:130px;width:580px;height:410px;background:linear-gradient(135deg,#e9e2d8 0%,#3a9bb5 50%,#1f4f88 100%);border-radius:240px 0 0 0}
.hero .desk{left:630px;top:570px;width:570px;height:103px;background:var(--grey-block);border-top:6px solid var(--navy)}

/* Platform band */
.platform{height:582px;background:linear-gradient(100deg,#c9551a 0%,var(--orange) 35%,var(--orange) 100%)}
.platform .art{left:245px;top:57px;width:250px;height:485px;border-radius:28px;background:linear-gradient(160deg,#f6f1e8,#e6dccd)}
.platform h2{left:600px;top:78px;width:520px;font-size:38px;line-height:43px;color:var(--white)}
.platform p{left:600px;top:230px;width:490px;font-size:15px;line-height:27px;color:#fde6d4}
.platform .btn{left:600px;top:433px;width:150px;height:55px;font-size:16px}

/* Solutions */
.solutions{height:562px;background:var(--white)}
.solutions .title{left:0;top:66px;width:1200px;text-align:center;font-size:38px}
.feature h3{font-size:34px;line-height:43px}
.solutions h3{left:111px;top:205px}
.solutions p{left:111px;top:275px;width:480px}
.solutions .art{left:610px;top:180px;width:590px;height:382px;background:linear-gradient(90deg,#7fb0a6 0%,#f0ebe3 50%,#8a2a3a 100%)}

.retention{height:512px;background:var(--beige)}
.retention .art{left:100px;top:38px;width:420px;height:430px;background:linear-gradient(160deg,#1f3a5f 0%,#7fbcb0 60%,#f8f4ec 100%)}
.retention h3{left:605px;top:138px}
.retention p{left:605px;top:203px;width:490px}

.planner{height:551px;background:var(--white)}
.planner h3{left:111px;top:106px;width:470px;font-size:33px !important}
.planner p{left:111px;top:276px;width:480px}
.planner .art{left:640px;top:81px;width:560px;height:390px;border-radius:12px 0 0 12px;background:linear-gradient(180deg,#e4ded3,#efeae2)}

.morale{height:513px;background:var(--cream)}
.morale .art{left:0;top:60px;width:580px;height:330px;background:linear-gradient(100deg,#2b4c7e 0%,#7fbcb0 50%,#f3a25e 100%)}
.morale .grey{left:0;top:390px;width:500px;height:123px;background:var(--grey-block);border-top:6px solid var(--navy)}
.morale h3{left:622px;top:135px}
.morale p{left:622px;top:205px;width:480px}

/* Why us */
.why{height:582px;background:var(--white)}
.why h2{left:111px;top:68px;font-size:38px}
.why p{left:111px;top:142px;width:460px}
.why ul{left:111px;top:246px;list-style:none;width:420px}
.why li{display:flex;gap:12px;font-size:17px;line-height:20px;margin-bottom:19px}
.why li svg{flex:none;margin-top:2px}
.why .btn{left:111px;top:457px;width:150px;height:51px;font-size:16px}
.why .art{left:615px;top:82px;width:473px;height:310px;border-radius:12px;background:linear-gradient(135deg,var(--orange),var(--orange-dark))}
.play{position:absolute;left:216px;top:135px}

/* Testimonials */
.testimonials{height:640px;background:var(--testi-bg)}
.testimonials h2{left:0;top:70px;width:1200px;text-align:center;font-size:38px}
.quote{left:270px;top:188px;width:660px;text-align:center;font-size:28px;line-height:42px;font-style:italic;font-weight:700;color:var(--ink)}
.author{left:0;top:455px;width:1200px;text-align:center;font-size:22px}
.photo{position:absolute;z-index:1;border-radius:50%;background:radial-gradient(circle at 50% 40%,#e8c9a8,#b8a48e)}
.photo.faded{opacity:.55}

/* CTA */
.cta{height:330px;background:linear-gradient(180deg,var(--orange-dark),var(--orange))}
.cta h2{left:0;top:72px;width:1200px;text-align:center;font-size:36px;line-height:43px;color:var(--white)}
.cta .btn-white{left:363px;top:190px;width:227px;height:65px;font-size:19px}
.cta .btn-outline{left:610px;top:190px;width:226px;height:65px;font-size:19px}

/* Footer */
.site-footer{height:374px;background:var(--white)}
.site-footer .logo{left:111px;top:40px;font-size:70px}
.contact{left:111px;font-size:17px;display:flex;align-items:center;gap:10px}
.col{top:68px}
.col h4{font-family:"Lexend",sans-serif;font-weight:500;font-size:18px;margin-bottom:22px}
.col a{display:block;color:var(--muted);font-size:15px;line-height:29px;text-decoration:none}
.divider{left:111px;top:280px;width:977px;height:1px;background:#ddd}
.copy{left:111px;top:322px;font-size:15px}
.social{left:955px;top:312px;display:flex;gap:14px}
.social span{width:36px;height:36px;border:1.5px solid var(--orange);border-radius:50%}
</style>
</head>
<body>

<header class="hero">
  <div class="abs logo">velquo</div>
  <nav class="abs nav"><span>About</span><span>Soluitons</span><span>Pricing</span><span>Blog</span><span>Contact</span></nav>
  <div class="abs login"><svg width="14" height="16" viewBox="0 0 14 16"><circle cx="7" cy="4.5" r="4" fill="#f47320"/><path d="M0 16c0-5 3-7 7-7s7 2 7 7z" fill="#f47320"/></svg>Login</div>
  <span class="btn btn-orange btn-nav">Request a demo</span>
  <h1 class="abs">Start building<br>your event today<br>with me!</h1>
  <span class="btn btn-orange btn-hero">Request a demo</span>
  <div class="art" role="img" aria-label="Illustration of a man working at a desktop computer with floating cards"></div>
  <div class="abs desk"></div>
</header>

<section class="platform">
  <div class="art" role="img" aria-label="Illustration of a smartphone showing the Velquo name"></div>
  <h2 class="abs">End-to-end employee recognition and retention Platform</h2>
  <p class="abs">Sed ut perspiciatis unde omnis iste natus error sit voluptam accusan tium doloremque laudantium, totam rem aperiam, eaque ipsa quaeab illo inventore veritatis et quasi architecto beatae vitae dicta sunt explica bo. Nemo enim ipsam vopta tem quia voluptas sit aspernatur aut odit aut fugit, sed quia consequuntur magni dolores eos.</p>
  <span class="btn btn-white">Read more</span>
</section>

<section class="solutions feature">
  <h2 class="abs title">Our <span class="accent">Solutions</span></h2>
  <h3 class="abs">Boost Employee Happiness</h3>
  <p class="abs body-text">Lorem ipsum dolor sit amet, consectetur adipiscinfrtg elit, sed do eiusmod tempor serincididunt ut labore et dolore magna aliqua. Ut enim ad minim veniamser quis nostrud exercitation ullamco laboris nisi ut aliquip ex ea commodo consequa aute irure dolor in reprehe.</p>
  <div class="art" role="img" aria-label="Illustration of two colleagues chatting, one holding a phone and one a coffee cup"></div>
</section>

<section class="retention feature">
  <div class="art" role="img" aria-label="Illustration of a smiling employee holding up an ID card"></div>
  <h3 class="abs">Increase Employee Retention</h3>
  <p class="abs body-text">Lorem ipsum dolor sit amet, consectetur adipiscinfrtg elit, sed do eiusmod tempor serincididunt ut labore et dolore magna aliqua. Ut enim ad minim veniamser quis nostrud exercitation ullamco laboris nisi ut aliquip ex ea commodo consequa aute irure dolor in reprehe.</p>
</section>

<section class="planner feature">
  <h3 class="abs">All-in-one Event Planner For Employee Appreciation Activity</h3>
  <p class="abs body-text">Lorem ipsum dolor sit amet, consectetur adipiscinfrtg elit, sed do eiusmod tempor serincididunt ut labore et dolore magna aliqua. Ut enim ad minim veniamser quis nostrud exercitation ullamco laboris nisi ut aliquip ex ea commodo consequa aute irure dolor in reprehe.</p>
  <div class="art" role="img" aria-label="Illustration of an event planner dashboard with contacts, schedule, calendar and tasks"></div>
</section>

<section class="morale feature">
  <div class="art" role="img" aria-label="Illustration of a man at a laptop with floating email, chat and calendar icons"></div>
  <div class="abs grey"></div>
  <h3 class="abs">Boost Employee Morale</h3>
  <p class="abs body-text">Lorem ipsum dolor sit amet, consectetur adipiscinfrtg elit, sed do eiusmod tempor serincididunt ut labore et dolore magna aliqua. Ut enim ad minim veniamser quis nostrud exercitation ullamco laboris nisi ut aliquip ex ea commodo consequa aute irure dolor in reprehe.</p>
</section>

<section class="why">
  <h2 class="abs">Why <span class="accent">Choose Us</span></h2>
  <p class="abs body-text">Lorem ipsum dolor sit amet, consectetur adipiscinfrtlit, sed do eiusmod tempor serincididunt ut labore dolore magna aliquim ad minim veniamser.</p>
  <ul class="abs">
    <li><svg width="16" height="16" viewBox="0 0 16 16"><circle cx="8" cy="8" r="7" fill="none" stroke="#f47320" stroke-width="2"/><path d="M4.5 8.2l2.4 2.3 4.6-4.8" fill="none" stroke="#f47320" stroke-width="2"/></svg>Maximum employee satisfaction</li>
    <li><svg width="16" height="16" viewBox="0 0 16 16"><circle cx="8" cy="8" r="7" fill="none" stroke="#f47320" stroke-width="2"/><path d="M4.5 8.2l2.4 2.3 4.6-4.8" fill="none" stroke="#f47320" stroke-width="2"/></svg>Employee engagement</li>
    <li><svg width="16" height="16" viewBox="0 0 16 16"><circle cx="8" cy="8" r="7" fill="none" stroke="#f47320" stroke-width="2"/><path d="M4.5 8.2l2.4 2.3 4.6-4.8" fill="none" stroke="#f47320" stroke-width="2"/></svg>Increase retention</li>
    <li><svg width="16" height="16" viewBox="0 0 16 16"><circle cx="8" cy="8" r="7" fill="none" stroke="#f47320" stroke-width="2"/><path d="M4.5 8.2l2.4 2.3 4.6-4.8" fill="none" stroke="#f47320" stroke-width="2"/></svg>Wellness, productivity, and culture in the workplace</li>
  </ul>
  <span class="btn btn-orange">Read more</span>
  <div class="art" role="img" aria-label="Video preview with a speech bubble reading Boost employee morale">
    <svg class="play" width="44" height="44" viewBox="0 0 44 44"><circle cx="22" cy="22" r="22" fill="#1b1b1b"/><path d="M17 13l14 9-14 9z" fill="#fff"/></svg>
  </div>
</section>

<section class="testimonials">
  <h2 class="abs">Client <span class="accent">Testimonials</span></h2>
  <div class="photo" style="left:62px;top:94px;width:182px;height:182px" role="img" aria-label="Portrait photo of a client"></div>
  <div class="photo faded" style="left:965px;top:53px;width:136px;height:136px" role="img" aria-label="Portrait photo of a client"></div>
  <div class="photo faded" style="left:62px;top:369px;width:132px;height:132px" role="img" aria-label="Portrait photo of a client"></div>
  <div class="photo faded" style="left:264px;top:456px;width:132px;height:132px" role="img" aria-label="Portrait photo of a client"></div>
  <div class="photo faded" style="left:923px;top:344px;width:206px;height:206px" role="img" aria-label="Portrait photo of a client"></div>
  <p class="abs quote">“ Duis aute irure dolor in reprehenderit in vo lup tate velit esse cillum dolore eu fugiat nulla paria tur. Excepteur sint occaecat cupid atat non proid ent, sunt in culpa qui officia deser aboprehenderit in rumnt”</p>
  <p class="abs author">- John Doe</p>
</section>

<section class="cta">
  <h2 class="abs">Try velquo with your team to create<br>a recognition-rich culture</h2>
  <span class="btn btn-white">Request a demo</span>
  <span class="btn btn-outline">Sign up now</span>
</section>

<footer class="site-footer">
  <div class="abs logo">velquo</div>
  <div class="abs contact" style="top:155px"><svg width="14" height="14" viewBox="0 0 14 14"><path d="M3 0l3 3-2 2c1 2 3 4 5 5l2-2 3 3-2 3C6 14 0 8 0 3z" fill="#f47320"/></svg>1 800 555 0142</div>
  <div class="abs contact" style="top:193px"><svg width="15" height="12" viewBox="0 0 15 12"><rect width="15" height="12" rx="1.5" fill="#f47320"/><path d="M1 1.5l6.5 5 6.5-5" fill="none" stroke="#fff" stroke-width="1.5"/></svg>info@velquo.com</div>
  <div class="abs col" style="left:505px"><h4>Explore</h4><a>About</a><a>Soluitons</a><a>Pricing</a><a>Blog</a><a>Contact</a></div>
  <div class="abs col" style="left:668px"><h4>Help Center</h4><a>Support</a></div>
  <div class="abs col" style="left:866px"><h4>Legal</h4><a>Privacy</a><a>Terms of Use</a></div>
  <div class="abs divider"></div>
  <div class="abs copy">© 2022, <b style="font-family:'Lexend',sans-serif">velquo</b>. All rights reseeved.</div>
  <div class="abs social"><span></span><span></span><span></span></div>
</footer>

</body>
</html>
```